Novarra clean Business Cards

I'm looking for someone to design my business card using my company name and logo. I would like it it be clean, fresh and a little out of the box. The colors I would like used are the same two in my logo (gold and the teal blue color) I also want it to screen high end scene the company name is Novarra clean :) I'm a commercial cleaning company based out of Orange and San Diego county. Once I receive your email I will send over the file. Because the file is quote big with several options of logos. Please be an out of the box thinker and take some risk...I'm looking for someone to put themselves out there. Thanks and good luck

```html
<!DOCTYPE html>
<html lang="en">
<head>
<meta charset="utf-8">
<title>Novarra Clean – Business Cards</title>
<link rel="stylesheet" href="https://fonts.googleapis.com/css2?family=Montserrat:wght@700&family=Questrial&family=Source+Sans+3:wght@400&display=swap">
<style>
  :root {
    --canvas: #ffffff;
    --brand-green: #0b764a;
    --brand-gold: #c9a94b;
    --brand-teal: #1a8fc4;
    --accent-red: #ed1c24;
    --navy-text: #2e3192;
    --email-yellow: #e6e21c;
    --white: #ffffff;
    --frame-blue: #29a8e0;
    --grad-light: #e4eef8;
    --grad-sky: #0aa0dc;
    --grad-deep: #1f3f96;
  }
  * { margin: 0; padding: 0; box-sizing: border-box; }
  html, body { width: 953px; height: 1200px; overflow: hidden; background: var(--canvas); }
  .canvas { position: relative; width: 953px; height: 1200px; }

  /* Front card */
  .card-front__header {
    position: absolute; left: 20px; top: 20px; width: 897px; height: 297px;
    background: var(--brand-green);
  }
  .brand-lockup {
    position: absolute; left: 0; right: 0; top: 150px;
    display: flex; align-items: center; justify-content: center; gap: 26px;
  }
  .brand-mark {
    width: 62px; height: 62px; flex: none;
    background: var(--brand-gold);
    border-bottom: 6px solid var(--brand-teal);
  }
  .brand-name {
    font-family: "Montserrat", sans-serif; font-weight: 700;
    font-size: 66px; letter-spacing: 4px; line-height: 1;
    color: var(--white); white-space: nowrap;
  }
  .brand-line {
    position: absolute; left: 0; right: 0; top: 232px;
    text-align: center;
    font-family: "Montserrat", sans-serif; font-weight: 700;
    font-size: 34px; letter-spacing: 5px; line-height: 1;
    color: var(--white); white-space: nowrap;
  }
  .card-front__rule {
    position: absolute; left: 20px; top: 315px; width: 897px; height: 14px;
    background: var(--accent-red);
  }
  .card-front__info {
    position: absolute; left: 20px; top: 329px; width: 897px; height: 196px;
    background: linear-gradient(90deg, var(--grad-light) 0%, var(--grad-sky) 50%, var(--grad-deep) 100%);
    border: 1px solid #8cc8ec;
    font-family: "Questrial", sans-serif;
  }
  .address {
    position: absolute; left: 77px; top: 43px;
    font-size: 20.5px; line-height: 31px; letter-spacing: 0.3px; color: var(--navy-text);
  }
  .phone {
    position: absolute; left: 77px; top: 123px;
    font-size: 20.5px; letter-spacing: 0.3px; color: var(--white);
  }
  .email {
    position: absolute; right: 37px; top: 123px;
    font-size: 20.5px; letter-spacing: 0.3px; color: var(--email-yellow);
  }
  .tagline {
    position: absolute; left: 0; right: 0; top: 153px; padding-left: 7px;
    text-align: center;
    font-family: "Source Sans 3", sans-serif; font-size: 23px; color: var(--white);
  }

  /* Back card */
  .card-back {
    position: absolute; left: 21px; top: 645px; width: 897px; height: 516px;
    border: 3px solid var(--frame-blue);
    background: linear-gradient(90deg, var(--grad-light) 0%, var(--grad-sky) 40%, var(--grad-deep) 100%);
    font-family: "Source Sans 3", sans-serif;
  }
  .services__title {
    position: absolute; left: 387px; top: 74px;
    font-size: 34px; color: var(--navy-text); font-weight: 400;
  }
  .services__list {
    position: absolute; left: 387px; top: 140px; list-style: none;
    font-size: 28.5px; line-height: 34.7px; color: var(--white);
  }
  .promise {
    position: absolute; left: 0; right: 0; top: 444px;
    text-align: center; font-size: 28px; color: var(--white);
  }
</style>
</head>
<body>
<main class="canvas">
  <section class="card-front" aria-label="Business card front">
    <header class="card-front__header">
      <div class="brand-lockup">
        <span class="brand-mark" aria-hidden="true"></span>
        <span class="brand-name">NOVARRA CLEAN</span>
      </div>
      <div class="brand-line">COMMERCIAL CLEANING SERVICES</div>
    </header>
    <div class="card-front__rule"></div>
    <div class="card-front__info">
      <p class="address">4417 Marlowe Ave. Lakewood<br>CA 90712</p>
      <p class="phone">Phone : 1(800)555-0147</p>
      <p class="email">Email : contact@novarracleancorp.com</p>
      <p class="tagline">"The Novarra Way to Clean"</p>
    </div>
  </section>

  <section class="card-back" aria-label="Business card back">
    <h2 class="services__title">Services :</h2>
    <ul class="services__list">
      <li>Construction Cleanup</li>
      <li>Power/Pressure Washing</li>
      <li>Strip and wax</li>
      <li>Carpet Cleaning</li>
      <li>Green Cleaning</li>
      <li>Scrub &amp; Finish</li>
      <li>Burnishing</li>
    </ul>
    <p class="promise">Hard work &amp; dedication is our promise to you!</p>
  </section>
</main>
</body>
</html>
```